Maple Hollow Canine Massage Needs a Business Card Design

Maple Hollow Canine Massage is a new therapeutic canine massage company located in Nederland, Colorado. I need a business card design that include my logo and basic contact information.

Target Market(s)

Pet owners, veterinarians

Industry/Entity Type

Business

Contact Information for Business Card

Lydia Ferrow, CCMT
303.518.7269
lydia@maplehollowmassage.example
www.maplehollowmassage.example

Colors
6c459b
886aae
b8a6cd
a64599
b768aa
d3a5cc
fbed22

Requirements
Must have
• Font should be similar to font in logo.

```html
<!DOCTYPE html>
<html lang="en">
<head>
<meta charset="utf-8">
<title>Maple Hollow Canine Massage – Business Card</title>
<link href="https://fonts.googleapis.com/css2?family=Montserrat:wght@600;700&family=Open+Sans:wght@400&display=swap" rel="stylesheet">
<style>
  :root{
    --page:#dfe4ea;
    --card-light:#eef2f6;
    --card-light-2:#d9e1ea;
    --ink:#0b0b0c;
    --ink-soft:#2f2f31;
    --gold:#d8d13a;
    --gold-deep:#b9ae1c;
    --purple:#6c459b;
    --purple-light:#886aae;
    --contact:#a9b3c6;
    --white:#f3f3f3;
  }
  html,body{margin:0;padding:0;overflow:hidden;}
  body{width:1200px;height:900px;background:var(--page);position:relative;}
  .card{
    position:absolute;left:100px;top:164px;width:1000px;height:572px;
    border-radius:22px;overflow:hidden;box-shadow:0 18px 40px rgba(0,0,0,.18);
  }
  .card-art{position:absolute;inset:0;}
  .holder{position:absolute;left:54px;top:204px;width:380px;}
  .holder-name{
    margin:0;font-family:"Montserrat",sans-serif;font-weight:700;
    font-size:36px;letter-spacing:.5px;color:var(--gold);line-height:1;
  }
  .holder-title{
    margin:9px 0 0;font-family:"Open Sans",sans-serif;font-size:19px;
    color:var(--white);line-height:1;
  }
  .contact-list{list-style:none;margin:20px 0 0;padding:0;}
  .contact-item{
    display:flex;align-items:center;gap:12px;
    font-family:"Open Sans",sans-serif;font-size:18px;color:var(--contact);
    letter-spacing:.3px;line-height:28px;white-space:nowrap;
  }
  .contact-icon{width:15px;height:15px;flex:none;}
  .brand{
    position:absolute;left:559px;top:97px;width:370px;height:370px;
    display:flex;flex-direction:column;align-items:center;justify-content:center;
    text-align:center;font-family:"Montserrat",sans-serif;font-weight:600;
    color:var(--gold);font-size:32px;line-height:1.15;letter-spacing:.5px;
  }
</style>
</head>
<body>
  <div class="card">
    <svg class="card-art" viewBox="0 0 1000 572" width="1000" height="572" aria-hidden="true">
      <defs>
        <linearGradient id="lightSide" x1="0" y1="0" x2="0" y2="1">
          <stop offset="0" stop-color="var(--card-light)"/>
          <stop offset="1" stop-color="var(--card-light-2)"/>
        </linearGradient>
        <radialGradient id="darkSide" cx="0.35" cy="0.2" r="0.9">
          <stop offset="0" stop-color="var(--ink-soft)"/>
          <stop offset="0.6" stop-color="var(--ink)"/>
          <stop offset="1" stop-color="#1c1c1e"/>
        </radialGradient>
        <linearGradient id="goldBand" x1="0" y1="0" x2="1" y2="1">
          <stop offset="0" stop-color="var(--gold-deep)"/>
          <stop offset="0.5" stop-color="var(--gold)"/>
          <stop offset="1" stop-color="var(--gold-deep)"/>
        </linearGradient>
        <linearGradient id="brandFill" x1="0" y1="0" x2="0" y2="1">
          <stop offset="0" stop-color="var(--purple-light)"/>
          <stop offset="1" stop-color="var(--purple)"/>
        </linearGradient>
      </defs>
      <rect class="card-base" width="1000" height="572" fill="url(#lightSide)"/>
      <path class="gold-crescent" fill="url(#goldBand)"
        d="M712 0 C560 60 452 170 452 286 C452 402 560 512 712 572 L730 572 C600 512 484 402 484 286 C484 170 600 60 730 0 Z"/>
      <path class="dark-panel" fill="url(#darkSide)"
        d="M0 0 H700 C555 60 452 170 452 286 C452 402 555 512 700 572 H0 Z"/>
      <circle class="brand-ring" cx="744" cy="282" r="196" fill="none" stroke="var(--gold)" stroke-width="4"/>
      <circle class="brand-disc" cx="744" cy="282" r="185" fill="url(#brandFill)"/>
    </svg>

    <div class="holder">
      <h1 class="holder-name">LYDIA FERROW</h1>
      <p class="holder-title">CCMT</p>
      <ul class="contact-list">
        <li class="contact-item">
          <svg class="contact-icon" viewBox="0 0 16 16"><path d="M4 1 L6.5 4.5 L5 6.5 C6 8.5 7.5 10 9.5 11 L11.5 9.5 L15 12 L13.5 15 C7 14.5 1.5 9 1 2.5 Z" fill="none" stroke="var(--gold)" stroke-width="1.4" stroke-linejoin="round"/></svg>
          <span>303.518.7269</span>
        </li>
        <li class="contact-item">
          <svg class="contact-icon" viewBox="0 0 16 16"><rect x="1" y="3" width="14" height="10" fill="none" stroke="var(--gold)" stroke-width="1.4"/><path d="M1 3 L8 9 L15 3" fill="none" stroke="var(--gold)" stroke-width="1.4"/></svg>
          <span>lydia@maplehollowmassage.example</span>
        </li>
        <li class="contact-item">
          <svg class="contact-icon" viewBox="0 0 16 16"><circle cx="8" cy="8" r="6.5" fill="none" stroke="var(--gold)" stroke-width="1.3"/><ellipse cx="8" cy="8" rx="3" ry="6.5" fill="none" stroke="var(--gold)" stroke-width="1.1"/><path d="M1.5 8 H14.5 M2.5 4.8 H13.5 M2.5 11.2 H13.5" stroke="var(--gold)" stroke-width="1.1"/></svg>
          <span>www.maplehollowmassage.example</span>
        </li>
      </ul>
    </div>

    <div class="brand">Maple Hollow<br>Canine Massage</div>
  </div>
</body>
</html>
```